Business card for new consulting business - Brenvale Holdings Pty Ltd.

Consulting in the areas of Occupational Health, Safety and Community Relations in the resources (mining) industries. The consultant (me) will work both within Australia and overseas jurisdictions such as South East Asia, Africa , South America etc, often working with third world indigenous communities. The design should suggest a high level of social and environmental responsibility.

```html
<!DOCTYPE html>
<html lang="en">
<head>
<meta charset="utf-8">
<title>Brenvale Holdings – Business Card</title>
<link rel="stylesheet" href="https://fonts.googleapis.com/css2?family=Roboto:wght@400;900&display=swap">
<style>
  :root {
    --backdrop: #cdcdcf;
    --card-white: #ffffff;
    --card-navy: #302f4f;
    --brand-blue: #4f95d2;
    --brand-green: #4db848;
    --tint-blue: rgba(79, 149, 210, 0.12);
    --tint-green: rgba(77, 184, 72, 0.12);
    --ink: #111111;
    --body-text: #555555;
  }
  * { box-sizing: border-box; margin: 0; padding: 0; }
  html, body { width: 960px; height: 1200px; overflow: hidden; }
  body {
    background: var(--backdrop);
    font-family: "Roboto", Arial, sans-serif;
    position: relative;
  }
  .card {
    position: absolute;
    left: 60px;
    width: 840px;
    height: 480px;
    overflow: hidden;
  }
  .card-front { top: 84px; background: var(--card-white); }
  .card-back  { top: 636px; background: var(--card-navy); }

  /* front: soft corner tint */
  .corner-tint {
    position: absolute;
    left: 0;
    top: 150px;
    width: 240px;
    height: 330px;
    background:
      radial-gradient(ellipse 75% 60% at 20% 70%, var(--tint-green), transparent 75%),
      radial-gradient(ellipse 70% 50% at 30% 25%, var(--tint-blue), transparent 75%);
  }

  /* front: brand name */
  .brand-front {
    position: absolute;
    left: 66px;
    top: 150px;
    width: 222px;
    text-align: center;
    color: var(--ink);
    font-weight: 900;
  }
  .brand-front .brand-main { display: block; font-size: 54px; line-height: 48px; letter-spacing: -1px; }
  .brand-front .brand-sub { display: block; font-size: 17px; line-height: 20px; letter-spacing: 3px; margin-top: 4px; }

  /* front: person */
  .person {
    position: absolute;
    right: 87px;
    top: 150px;
    text-align: right;
  }
  .person-name {
    font-weight: 900;
    font-size: 38px;
    letter-spacing: 1px;
    color: var(--brand-blue);
    line-height: 40px;
  }
  .person-role {
    font-weight: 900;
    font-size: 21px;
    line-height: 24px;
    color: var(--brand-green);
    margin-top: 2px;
    letter-spacing: 0.3px;
  }
  .accent-bar {
    position: absolute;
    left: 773px;
    top: 158px;
    width: 67px;
    height: 23px;
    background: var(--brand-blue);
  }

  /* front: contacts */
  .contact {
    position: absolute;
    top: 354px;
    font-size: 17.5px;
    line-height: 20px;
    color: var(--body-text);
  }
  .contact-icon {
    position: absolute;
    width: 20px; height: 20px;
  }
  .contact-street { left: 46px; }
  .contact-street p { margin-left: 47px; }
  .contact-postal { left: 297px; }
  .contact-postal p { margin-left: 46px; }
  .contact-direct { left: 534px; top: 354px; }
  .contact-line { position: relative; height: 32px; padding-left: 64px; }
  .contact-line .contact-icon { left: 18px; top: 0; }
  .abn-label {
    position: absolute;
    left: 10px;
    color: var(--brand-blue);
    font-size: 16px;
  }

  /* back */
  .brand-back {
    position: absolute;
    inset: 0;
    display: flex;
    flex-direction: column;
    align-items: center;
    justify-content: center;
    color: var(--card-white);
    text-align: center;
    font-weight: 900;
  }
  .brand-back .brand-main { font-size: 110px; line-height: 96px; letter-spacing: -2px; }
  .brand-back .brand-sub { font-size: 34px; line-height: 40px; letter-spacing: 5px; margin-top: 14px; }
</style>
</head>
<body>

<section class="card card-front">
  <div class="corner-tint" role="img" aria-label="Soft blue and green background tint"></div>

  <div class="brand-front">
    <span class="brand-main">Brenvale</span>
    <span class="brand-sub">HOLDINGS</span>
  </div>

  <div class="person">
    <p class="person-name">MARCUS ELLERY</p>
    <p class="person-role">DIRECTOR</p>
  </div>
  <div class="accent-bar"></div>

  <div class="contact contact-street">
    <svg class="contact-icon" viewBox="0 0 20 20" style="left:0;top:0" aria-hidden="true">
      <circle cx="10" cy="10" r="10" fill="var(--brand-blue)"/>
      <path d="M4.5 10.5 L10 5.5 L15.5 10.5 M6.5 9.5 V14.5 H13.5 V9.5" fill="none" stroke="#fff" stroke-width="1.6" stroke-linejoin="round"/>
      <rect x="8.8" y="11" width="2.4" height="3.5" fill="#fff"/>
    </svg>
    <p>41 Kestrel Street,<br>Sorrento,<br>Western Australia,<br>Australia 6020</p>
  </div>

  <div class="contact contact-postal">
    <svg class="contact-icon" viewBox="0 0 20 20" style="left:0;top:0" aria-hidden="true">
      <circle cx="10" cy="10" r="10" fill="var(--brand-blue)"/>
      <rect x="4.5" y="6.5" width="11" height="7.5" rx="1.5" fill="none" stroke="#fff" stroke-width="1.5"/>
      <rect x="10" y="8.5" width="3.5" height="2.5" fill="#fff"/>
    </svg>
    <p>PO Box 512 Duncraig,<br>Western Australia,<br>Australia 6916</p>
  </div>

  <div class="contact contact-direct">
    <div class="contact-line">
      <svg class="contact-icon" viewBox="0 0 20 20" aria-hidden="true">
        <circle cx="10" cy="10" r="10" fill="var(--brand-blue)"/>
        <path d="M7 4.5 C5 5.5 5 9 7 12 C9 15 11.5 16 13.5 15 L12.2 12.3 L10.8 12.8 C9.6 11.8 8.6 10 8.4 8.4 L9.6 7.6 Z" fill="#fff"/>
      </svg>
      +61 412 555 318
    </div>
    <div class="contact-line">
      <svg class="contact-icon" viewBox="0 0 20 20" aria-hidden="true">
        <circle cx="10" cy="10" r="10" fill="var(--brand-blue)"/>
        <rect x="4.5" y="6.5" width="11" height="7.5" rx="1" fill="none" stroke="#fff" stroke-width="1.4"/>
        <path d="M4.8 7 L10 11 L15.2 7" fill="none" stroke="#fff" stroke-width="1.4"/>
      </svg>
      marcus@ellery.net.au
    </div>
    <div class="contact-line">
      <span class="abn-label">ABN</span>
      51 824 309 617
    </div>
  </div>
</section>

<section class="card card-back">
  <div class="brand-back">
    <span class="brand-main">Brenvale</span>
    <span class="brand-sub">HOLDINGS</span>
  </div>
</section>

</body>
</html>
```